Book design for Martial Arts Business

TITLE : The Lantern Ledger Method

Subtitle : " Master your business , Master your life

Author Hollis Penwarden

I need a book cover design for my new book which is on Martial Arts Busines Success.

Simple and Powerful Black and red in Design
Strong font , thats clear and easy to read
the Tag line of the book is " Master your business, Master your life ( I want this to stand out )

Front cover image with dojo

Back image of myself

space for 2 endorsement and writing about the book

I dont want it to look cheesy or American must have an uk feel too

No money on the book whatsoever

I have attached a design so far for you to see but want variations
Updates

Reason: Not quite got the look on this we will have to extend this

Need extra days to review

Need extra days to review

Target Market(s)

Martial Arts Business owners

Industry/Entity Type

Business

Colors
000000
ec1f27

Requirements
Must have
• Red and Black in colour
• good font thats not standard .. Impactful and clear
• Images used and any other ideas
Nice to have
• No money in it
Should not have
• Clear and powerful design

```html
<!DOCTYPE html>
<html lang="en">
<head>
<meta charset="utf-8">
<title>The Lantern Ledger Method – Book Cover</title>
<link rel="stylesheet" href="https://fonts.googleapis.com/css2?family=Stardos+Stencil:wght@700&family=Roboto+Condensed:wght@700&family=Cinzel:wght@400&display=swap">
<style>
  :root {
    --ink: #000000;
    --red: #ec1f27;
    --paper: #ffffff;
    --stage: #b6b6b6;
    --title-font: "Stardos Stencil", "Impact", sans-serif;
    --tag-font: "Roboto Condensed", "Arial Narrow", sans-serif;
    --author-font: "Cinzel", "Times New Roman", serif;
  }
  html, body {
    margin: 0;
    width: 1200px;
    height: 1200px;
    overflow: hidden;
    background: var(--stage);
  }
  .book-cover {
    position: absolute;
    left: 250px;
    top: 60px;
    width: 700px;
    height: 1080px;
    background: var(--paper);
    overflow: hidden;
    box-shadow: 0 20px 40px rgba(0,0,0,0.18);
  }
  .cover-base {
    position: absolute;
    left: 0;
    top: 880px;
    width: 100%;
    height: 200px;
    background: var(--ink);
  }
  .author-portrait {
    position: absolute;
    left: 430px;
    top: 80px;
    width: 270px;
    height: 1000px;
    background: linear-gradient(180deg, #d9c2b0 0%, #c9a893 22%, #1b1b1b 36%, #111 70%, #0a0a0a 100%);
  }
  .cover-title {
    position: absolute;
    left: 0;
    top: 0;
    width: 430px;
    height: 680px;
  }
  .title-black { fill: var(--ink); font-family: var(--title-font); font-weight: 700; }
  .title-red { fill: var(--red); font-family: var(--title-font); font-weight: 700; }
  .tagline-band {
    position: absolute;
    left: 0;
    top: 740px;
    width: 430px;
    height: 140px;
    background: var(--red);
  }
  .tagline {
    position: absolute;
    left: 152px;
    top: 772px;
    margin: 0;
    color: var(--paper);
    font-family: var(--tag-font);
    font-weight: 700;
    font-size: 28px;
    line-height: 1.1;
  }
  .dojo-inset {
    position: absolute;
    left: -10px;
    top: 705px;
    width: 150px;
    height: 150px;
    border: 4px solid var(--ink);
    background: linear-gradient(180deg, #e9e2d8 0%, #d8c9c0 40%, #cf3b44 62%, #e8a0b0 100%);
    transform: rotate(-4deg);
  }
  .author-name {
    position: absolute;
    left: 40px;
    top: 992px;
    margin: 0;
    color: var(--paper);
    font-family: var(--author-font);
    font-size: 33px;
    letter-spacing: 1px;
  }
</style>
</head>
<body>
  <main class="book-cover">
    <div class="cover-base"></div>
    <div class="author-portrait" role="img" aria-label="Photograph of the author smiling in a black sleeveless training top and black belt"></div>

    <svg class="cover-title" viewBox="0 0 430 680" aria-label="The Lantern Ledger Method">
      <text class="title-black" x="150" y="185" font-size="70" textLength="140" lengthAdjust="spacingAndGlyphs">THE</text>
      <text class="title-black" x="30" y="310" font-size="128" textLength="380" lengthAdjust="spacingAndGlyphs">LANTERN</text>
      <text class="title-red" x="35" y="470" font-size="120" textLength="360" lengthAdjust="spacingAndGlyphs">LEDGER</text>
      <text class="title-red" x="25" y="650" font-size="170" textLength="375" lengthAdjust="spacingAndGlyphs">METHOD</text>
    </svg>

    <div class="tagline-band"></div>
    <p class="tagline">Master your business,<br>Master your life</p>
    <div class="dojo-inset" role="img" aria-label="Photograph of students in red uniforms training in a dojo"></div>

    <p class="author-name">Hollis Penwarden</p>
  </main>
</body>
</html>
```